Clearstep Podiatry Care Advertisement Sandwich board

We need a Sandwich board design for our fungal nail clinic - please find attached the sandwich board dimensions.

The sandwich board itself will be displayed outside of a large health clinic and we need it to attract the attention of people walking by. We need a brochure holder included in the design which will hold our brochures which provides as clients with more information (please see attached also).

We are open to the designers creativity but we would like a similar theme portrayed on our board that is similar to our website (www.clearsteppodiatrycare.co.nz) and brochure that incorporates our logo which I have attached). The final design should communicate professionalism and be a minimalist look but modern to capture the attention of pedestrians.

Finally, we would like the website and phone number (07) 382 5164.

We look forward to seeing your work.

```html
<!DOCTYPE html>
<html lang="en">
<head>
<meta charset="utf-8">
<title>Clearstep Podiatry Care – Sandwich Board</title>
<link href="https://fonts.googleapis.com/css2?family=Bebas+Neue&family=Montserrat:wght@500;700;800&display=swap" rel="stylesheet">
<style>
  :root {
    --brand-blue: #3d67ae;
    --ink: #1c1c1c;
    --white: #ffffff;
    --slot-grey: #787878;
    --ring-grey: #a9a9a9;
    --backdrop: #7a7a7a;
    --skin-light: #f1ddd0;
    --skin-mid: #e6bfa5;
  }
  * { margin: 0; padding: 0; box-sizing: border-box; }
  html, body {
    width: 1200px; height: 2252px; overflow: hidden;
    background: var(--backdrop);
  }
  .board {
    position: absolute; left: 60px; top: 442px;
    width: 730px; height: 925px;
    transform: scale(1.4795); transform-origin: top left;
    background: linear-gradient(160deg, #fafafa 0%, #eeeeee 100%);
    overflow: hidden;
    box-shadow: 0 6px 14px rgba(0,0,0,.35);
    font-family: "Montserrat", sans-serif;
  }
  .board__art { position: absolute; inset: 0; width: 730px; height: 925px; }
  .brochure-slot {
    position: absolute; left: 306px; top: 47px; width: 132px; height: 36px;
    border-radius: 18px; background: var(--slot-grey);
  }
  .brand-mark {
    position: absolute; left: 80px; top: 48px; width: 192px; height: 192px;
    border-radius: 50%; background: var(--brand-blue);
    border: 12px solid var(--ring-grey);
  }
  .brand-name {
    position: absolute; left: 296px; top: 120px; width: 170px;
    font-weight: 700; font-size: 22px; line-height: 1.15; color: var(--brand-blue);
  }
  .headline {
    position: absolute; left: 46px; top: 296px;
    font-family: "Bebas Neue", sans-serif; font-weight: 400;
    font-size: 86px; line-height: 76px; color: var(--white);
  }
  .headline .dark { color: var(--ink); }
  .tagline {
    position: absolute; left: 50px; top: 538px;
    font-weight: 800; font-size: 27px; line-height: 32px; color: var(--ink);
  }
  .pill {
    position: absolute; display: flex; align-items: center;
    border-radius: 24px; font-family: "Bebas Neue", sans-serif;
  }
  .pill--treatments {
    left: 48px; top: 613px; width: 232px; height: 42px;
    background: var(--white); color: var(--brand-blue);
    justify-content: center; font-size: 28px;
  }
  .treatments {
    position: absolute; left: 48px; top: 665px; list-style: none;
    color: var(--white); font-weight: 500; font-size: 21px;
  }
  .treatments li { display: flex; align-items: center; height: 30.5px; }
  .treatments svg { width: 18px; height: 18px; margin-right: 14px; }
  .pill--phone {
    left: 48px; top: 832px; width: 232px; height: 44px;
    background: var(--white); color: var(--ink); font-size: 32px;
    padding-left: 6px; gap: 10px;
  }
  .pill--web {
    left: 308px; top: 832px; width: 382px; height: 44px;
    background: var(--brand-blue); border: 3px solid var(--white);
    color: var(--white); font-size: 27px; padding-left: 5px; gap: 10px;
  }
  .pill svg { width: 32px; height: 32px; flex: none; }
</style>
</head>
<body>
<div class="board">
  <svg class="board__art" viewBox="0 0 730 925" xmlns="http://www.w3.org/2000/svg">
    <defs>
      <linearGradient id="photoTone" x1="0" y1="0" x2="1" y2="1">
        <stop offset="0" stop-color="#f7f4f2"/>
        <stop offset=".5" stop-color="var(--skin-light)"/>
        <stop offset="1" stop-color="var(--skin-mid)"/>
      </linearGradient>
    </defs>
    <rect class="photo" role="img" aria-label="Photo of a woman's smooth bare legs standing on tiptoe, hands resting on the thigh"
          x="300" y="0" width="430" height="925" fill="url(#photoTone)"/>
    <path class="wave" fill="var(--brand-blue)"
          d="M0 0 H80 C58 50 38 130 52 180 C70 240 150 268 240 282 C340 298 418 335 425 420 C432 500 360 600 330 700 C420 660 500 700 495 780 C490 850 380 900 290 925 H0 Z"/>
    <path fill="none" stroke="var(--white)" stroke-width="5"
          d="M70 60 C50 120 40 170 60 205 C90 250 170 272 260 288 C350 305 400 340 405 420"/>
    <path fill="none" stroke="var(--white)" stroke-width="5"
          d="M450 700 C480 740 470 820 410 870 C380 895 340 915 300 925"/>
  </svg>

  <div class="brochure-slot"></div>
  <div class="brand-mark"></div>
  <div class="brand-name">Clearstep Podiatry Care</div>

  <h1 class="headline">Clearstep<br><span class="dark">Podiatry</span><br>Care</h1>
  <p class="tagline">YOUR FUNGAL<br>NAIL EXPERT</p>

  <div class="pill pill--treatments">Treatments Offered</div>
  <ul class="treatments">
    <li><svg viewBox="0 0 20 20"><circle cx="10" cy="10" r="8" fill="none" stroke="#1c1c1c" stroke-width="1.6"/><path d="M6 10 l3 3 l6 -7" fill="none" stroke="#1c1c1c" stroke-width="1.8"/></svg>Cold Laser</li>
    <li><svg viewBox="0 0 20 20"><circle cx="10" cy="10" r="8" fill="none" stroke="#1c1c1c" stroke-width="1.6"/><path d="M6 10 l3 3 l6 -7" fill="none" stroke="#1c1c1c" stroke-width="1.8"/></svg>Topical</li>
    <li><svg viewBox="0 0 20 20"><circle cx="10" cy="10" r="8" fill="none" stroke="#1c1c1c" stroke-width="1.6"/><path d="M6 10 l3 3 l6 -7" fill="none" stroke="#1c1c1c" stroke-width="1.8"/></svg>General Nail Care</li>
    <li><svg viewBox="0 0 20 20"><circle cx="10" cy="10" r="8" fill="none" stroke="#1c1c1c" stroke-width="1.6"/><path d="M6 10 l3 3 l6 -7" fill="none" stroke="#1c1c1c" stroke-width="1.8"/></svg>Oral</li>
    <li><svg viewBox="0 0 20 20"><circle cx="10" cy="10" r="8" fill="none" stroke="#1c1c1c" stroke-width="1.6"/><path d="M6 10 l3 3 l6 -7" fill="none" stroke="#1c1c1c" stroke-width="1.8"/></svg>Surgery</li>
  </ul>

  <div class="pill pill--phone">
    <svg viewBox="0 0 32 32"><circle cx="16" cy="16" r="15" fill="var(--brand-blue)"/><path d="M11 8 l3 0 l1.5 4 l-2 1.5 c1 2.5 2.5 4 5 5 l1.5 -2 l4 1.5 l0 3 c-8 1 -14 -5 -13 -13 z" fill="#fff"/></svg>
    (07) 382 5164
  </div>
  <div class="pill pill--web">
    <svg viewBox="0 0 32 32"><circle cx="16" cy="16" r="14" fill="#fff"/><circle cx="16" cy="16" r="8" fill="none" stroke="var(--ink)" stroke-width="1.6"/><path d="M8 16 h16 M16 8 c-4 4 -4 12 0 16 M16 8 c4 4 4 12 0 16" fill="none" stroke="var(--ink)" stroke-width="1.4"/></svg>
    WWW.CLEARSTEPPODIATRYCARE.CO.NZ
  </div>
</div>
</body>
</html>
```